Birchwood Claims Services
Property Claims Management, Catastrophe Services
Birchwood Claims Services -
Creative Brief
Professional
Tom Fenwick
President
4817 Copper Mill Lane Dunmore Township, PA 18519
tom@birchwoodclaimservices.example
birchwoodclaimservices.example

```html
<!DOCTYPE html>
<html lang="en">
<head>
<meta charset="utf-8">
<title>Birchwood Claims Services — Business Card</title>
<link href="https://fonts.googleapis.com/css2?family=PT+Serif:wght@400;700&display=swap" rel="stylesheet">
<style>
  :root {
    --backdrop: #e9e6e1;
    --card: #ffffff;
    --brand-green: #1f8a3c;
    --deep-green: #17632c;
    --ink: #3b3b3b;
    --faint-green: #e6f1ea;
  }
  html, body {
    margin: 0;
    width: 1200px;
    height: 852px;
    overflow: hidden;
    background: var(--backdrop);
    font-family: "PT Serif", Georgia, serif;
  }
  .canvas {
    position: relative;
    width: 1200px;
    height: 852px;
  }
  .business-card {
    position: absolute;
    left: 100px;
    top: 140px;
    width: 1000px;
    height: 572px;
    background: var(--card);
    border-radius: 34px;
    box-shadow: 0 10px 30px rgba(0,0,0,0.18);
    overflow: hidden;
  }
  .decor-circle {
    position: absolute;
    right: -60px;
    top: 10px;
    width: 380px;
    height: 380px;
    border-radius: 50%;
    border: 36px solid var(--faint-green);
    box-sizing: border-box;
  }
  .brand {
    position: absolute;
    left: 70px;
    top: 58px;
    display: flex;
    align-items: center;
    gap: 22px;
  }
  .brand-mark {
    width: 92px;
    height: 92px;
    border-radius: 50%;
    background: var(--brand-green);
  }
  .brand-name {
    font-size: 40px;
    font-weight: 400;
    color: var(--brand-green);
    line-height: 1.1;
    max-width: 420px;
  }
  .address {
    position: absolute;
    left: 82px;
    top: 262px;
    font-size: 22px;
    line-height: 1.35;
    color: var(--ink);
    margin: 0;
  }
  .contacts {
    position: absolute;
    left: 82px;
    top: 350px;
    margin: 0;
    padding: 0;
    list-style: none;
    font-size: 21px;
    color: var(--ink);
  }
  .contacts li {
    display: flex;
    align-items: center;
    gap: 14px;
    height: 38px;
  }
  .contacts svg {
    width: 24px;
    height: 24px;
    flex: none;
  }
  .person {
    position: absolute;
    right: 140px;
    top: 188px;
    text-align: right;
  }
  .person-name {
    font-size: 32px;
    font-weight: 700;
    color: var(--deep-green);
    margin: 0;
  }
  .person-title {
    font-size: 21px;
    color: var(--ink);
    margin: 4px 0 0;
  }
</style>
</head>
<body>
<main class="canvas">
  <section class="business-card">
    <div class="decor-circle" aria-hidden="true"></div>

    <div class="brand">
      <div class="brand-mark" aria-hidden="true"></div>
      <div class="brand-name">Birchwood Claims Services</div>
    </div>

    <p class="address">4817 Copper Mill Lane<br>Dunmore Township, PA 18519</p>

    <ul class="contacts">
      <li>
        <svg viewBox="0 0 24 24" aria-hidden="true">
          <path d="M6.6 3.5c.6-.4 1.4-.3 1.8.3l2 3c.4.6.3 1.3-.2 1.8l-1.3 1.1c.9 2 2.5 3.6 4.5 4.5l1.1-1.3c.5-.5 1.2-.6 1.8-.2l3 2c.6.4.7 1.2.3 1.8l-1.2 1.8c-.5.7-1.4 1-2.2.8C10.7 17.6 6.4 13.3 4.9 7.8c-.2-.8.1-1.7.8-2.2z" fill="var(--deep-green)"/>
        </svg>
        <span>(570) 555-0148</span>
      </li>
      <li>
        <svg viewBox="0 0 24 24" aria-hidden="true">
          <circle cx="12" cy="12" r="11" fill="var(--brand-green)"/>
          <circle cx="12" cy="12" r="3.4" fill="none" stroke="#fff" stroke-width="1.8"/>
          <path d="M15.4 9v4.2c0 1.3 1.9 1.5 2.2 0 .6-3.4-1.7-6.6-5.6-6.6a5.4 5.4 0 1 0 3 9.9" fill="none" stroke="#fff" stroke-width="1.8" stroke-linecap="round"/>
        </svg>
        <span>tom@birchwoodclaimservices.example</span>
      </li>
      <li>
        <svg viewBox="0 0 24 24" aria-hidden="true">
          <circle cx="12" cy="12" r="11" fill="var(--brand-green)"/>
          <circle cx="12" cy="12" r="6.5" fill="none" stroke="#fff" stroke-width="1.4"/>
          <ellipse cx="12" cy="12" rx="2.8" ry="6.5" fill="none" stroke="#fff" stroke-width="1.4"/>
          <line x1="5.5" y1="12" x2="18.5" y2="12" stroke="#fff" stroke-width="1.4"/>
        </svg>
        <span>birchwoodclaimservices.example</span>
      </li>
    </ul>

    <div class="person">
      <p class="person-name">Tom Fenwick</p>
      <p class="person-title">President</p>
    </div>
  </section>
</main>
</body>
</html>
```